In Dash GPS

My Business is a small family owned and operated company.
Our specialty is In dash GPS systems.
These systems are All touch screen with built in bluetooth, AM/FM RDS radio, GPS, USB, Media player integration, DVD/MP3/CD/SD, steering wheel controls still work.
Product is installed by a experienced installer, and is local.
ALL MAKES AND MODELS AVAILABLE!
I do a lot of work for car dealerships and private buyers..
These are some of my competitors websites:
http://www.routelynxhub.com.au/index.php
http://www.velmo.com.au/Integrated-GPS-Systems-s/582.htm
http://www.auto-spexa.co.uk/226-kalden-navi-dvd
Im looking for a flyer I can put up in car dealerships to advertise the different work I can offer.
I have attached a copy of my business card and logo for your convenience.
The colours on the business card are the main ones I want to use.
I have also uploaded some of the work I have done
NEW and USED car buyers, private buyers
Wheel

```html
<!DOCTYPE html>
<html lang="en">
<head>
<meta charset="utf-8">
<title>Tavener Creations – Push the Button and Drive!</title>
<link rel="stylesheet" href="https://fonts.googleapis.com/css2?family=Alfa+Slab+One&family=Open+Sans:wght@400&display=swap">
<style>
  :root {
    --navy-top: #223a52;
    --navy-mid: #18283a;
    --navy-deep: #121820;
    --band: #141414;
    --glow: #3ab8f0;
    --glow-soft: rgba(58, 184, 240, 0.55);
    --heading-fill: #182434;
    --text: #ffffff;
    --rule: #ffffff;
  }
  * { margin: 0; padding: 0; box-sizing: border-box; }
  html, body { width: 1200px; height: 846px; overflow: hidden; background: var(--band); }
  .flyer {
    position: relative;
    width: 1200px;
    height: 846px;
    overflow: hidden;
    font-family: "Open Sans", Arial, sans-serif;
    color: var(--text);
    background: linear-gradient(180deg, var(--navy-top) 0%, var(--navy-mid) 40%, var(--navy-deep) 79.5%);
  }
  .brand-name {
    position: absolute;
    top: 108px;
    right: 72px;
    font-weight: 400;
    font-size: 36px;
    line-height: 1;
    color: var(--text);
    white-space: nowrap;
  }
  .power-icon {
    position: absolute;
    left: 90px;
    top: 266px;
    width: 236px;
    height: 236px;
  }
  .headline {
    position: absolute;
    left: 380px;
    top: 268px;
    width: 750px;
    text-align: center;
    font-family: "Alfa Slab One", Georgia, serif;
    font-weight: 400;
    color: var(--heading-fill);
    -webkit-text-stroke: 2px var(--glow);
    text-shadow: 0 0 10px var(--glow-soft), 0 0 18px var(--glow-soft);
    line-height: 1;
    white-space: nowrap;
  }
  .headline-top { display: block; font-size: 66px; letter-spacing: 1px; }
  .headline-bottom { display: block; font-size: 120px; margin-top: 4px; }
  .features {
    position: absolute;
    left: 0;
    top: 566px;
    width: 1200px;
    text-align: center;
    font-size: 31px;
    line-height: 42px;
    white-space: nowrap;
  }
  .divider {
    position: absolute;
    left: 0;
    top: 671px;
    width: 1200px;
    height: 7px;
    background: var(--rule);
  }
  .contact-band {
    position: absolute;
    left: 0;
    top: 678px;
    width: 1200px;
    height: 168px;
    background: var(--band);
  }
  .contact {
    position: absolute;
    left: 0;
    top: 742px;
    width: 1200px;
    text-align: center;
    font-size: 27px;
  }
</style>
</head>
<body>
<main class="flyer">
  <header>
    <p class="brand-name">Tavener Creations</p>
  </header>

  <svg class="power-icon" viewBox="0 0 240 240" aria-hidden="true">
    <defs>
      <filter id="glow" x="-30%" y="-30%" width="160%" height="160%">
        <feGaussianBlur stdDeviation="5" result="b"/>
        <feMerge><feMergeNode in="b"/><feMergeNode in="SourceGraphic"/></feMerge>
      </filter>
    </defs>
    <g filter="url(#glow)" fill="none" stroke="#3ab8f0" stroke-width="3">
      <circle cx="120" cy="120" r="114"/>
      <circle cx="120" cy="120" r="90"/>
    </g>
    <circle cx="120" cy="120" r="102" fill="none" stroke="#131c28" stroke-width="21"/>
    <g filter="url(#glow)" fill="#131c28" stroke="#3ab8f0" stroke-width="3" stroke-linejoin="round">
      <path d="M92 82 A56 56 0 1 0 148 82 L140 98 A40 40 0 1 1 100 98 Z"/>
      <rect x="110" y="40" width="20" height="82" rx="10"/>
    </g>
  </svg>

  <h1 class="headline">
    <span class="headline-top">PUSH THE BUTTON</span>
    <span class="headline-bottom">and DRIVE!</span>
  </h1>

  <p class="features">All touch screen with built in bluetooth, AM/FM RDS radio, GPS, USB,<br>Media player integration, DVD/MP3/CD/SD, steering wheel controls still work</p>

  <div class="divider"></div>
  <div class="contact-band"></div>
  <p class="contact">Dan Tavener | 0400 555 218 | dantavener@example.com</p>
</main>
</body>
</html>
```